BRAMLEIGH real estate family office

Hello, Our business is a real estate intermediation activity on high-end goods (amounts exceeding € 10m) for corporate and private clients. You can see our logo on the site www.bramleigh-estates.fr We would like to keep that spirit with the hexagon that represents France (transactions between Monaco and Saint Tropez, Courchevel and Paris). And the "baseline" that is "real estate family office". The corporate logo should be and can be printed by embossing (relief). We must integrate the name, first name, phone, email and website. Finally, to imbibe the spirit of business, here is a detail of the activity. "Genuine consulting firm in real estate investments, BRAMLEIGH works with its customers as a specialized player in the high-end markets, we are recognized for our ultra-confidential approach and tailor-made, as well as the quality of our network. We broadcast any information on the market and we work exclusively through a strong relationship we have developed over the years. BRAMLEIGH is active on the French Riviera (from Monaco to Saint-Tropez), the Alps (Courchevel, Méribel, Megève) and Paris (essentially market premium). Always looking for opportunities for our clients, we work on two investment areas: residential luxury real estate (properties, vineyards, mansions, land, etc.) commercial real estate (empty office buildings or yield, hotel properties, land, etc.) "

Target Market(s)

High foreign end customers. corporate and private.

Industry/Entity Type

Real Estate

Contact Information for Business Card

LOGO
baseline
Thibault Marchand
+33(0)6.41.57.94.16
tm@bramleigh-estates.fr
www.bramleigh-estates.fr

Font styles to use
Serif

Colors
cedeed
0255a3
3277b5
85abd2
85cae6
34a7d7
0792cd
cfdeed
1b1b1b

Requirements
Must have
• see description

```html
<!DOCTYPE html>
<html lang="en">
<head>
<meta charset="utf-8">
<title>BRAMLEIGH – Business Card</title>
<link rel="stylesheet" href="https://fonts.googleapis.com/css2?family=Questrial&family=Arimo:wght@400;700&display=swap">
<style>
  :root {
    --bg: #e9ecf0;
    --royal: #0255a3;
    --royal-deep: #053f85;
    --royal-light: #3277b5;
    --sky: #85abd2;
    --paper: #ffffff;
    --paper-shade: #f1f2f4;
    --frame-grey: #8c8f94;
    --logo-grey: #6d7075;
    --ink: #1b1b1b;
  }
  * { margin: 0; padding: 0; box-sizing: border-box; }
  html, body { width: 1200px; height: 843px; overflow: hidden; }
  body {
    background: var(--bg);
    position: relative;
    font-family: "Arimo", Arial, sans-serif;
  }
  .card {
    position: absolute;
    top: 266px;
    width: 540px;
    height: 310px;
    overflow: hidden;
    box-shadow: 0 6px 18px rgba(0, 0, 0, 0.18);
  }

  /* Back of the card */
  .card--back {
    left: 40px;
    background: linear-gradient(160deg, var(--royal-light) 0%, var(--royal) 45%, var(--royal-deep) 100%);
  }
  .card--back .wordmark {
    position: absolute;
    left: 0; right: 0; top: 104px;
    text-align: center;
    font-family: "Questrial", "Century Gothic", sans-serif;
    font-size: 48px;
    letter-spacing: 5px;
    color: var(--paper);
    line-height: 1;
  }
  .card--back .baseline {
    position: absolute;
    right: 108px; top: 158px;
    font-family: "Questrial", "Century Gothic", sans-serif;
    font-size: 15px;
    color: var(--sky);
  }
  .card--back .web {
    position: absolute;
    left: 0; right: 0; top: 220px;
    text-align: center;
    font-size: 13px;
    letter-spacing: 7px;
    color: var(--paper);
  }

  /* Front of the card */
  .card--front {
    left: 620px;
    background: linear-gradient(200deg, var(--paper) 0%, var(--paper) 55%, var(--paper-shade) 100%);
  }
  .card--front .wordmark {
    position: absolute;
    left: 36px; top: 38px;
    font-family: "Questrial", "Century Gothic", sans-serif;
    font-size: 44px;
    letter-spacing: 4px;
    color: var(--logo-grey);
    line-height: 1;
  }
  .card--front .baseline {
    position: absolute;
    left: 146px; top: 88px;
    font-family: "Questrial", "Century Gothic", sans-serif;
    font-size: 14px;
    color: var(--royal);
  }
  .contact-panel {
    position: absolute;
    left: 286px; top: 138px;
    width: 280px; height: 200px;
    background: var(--royal);
    border: 3px solid var(--paper);
    outline: 4px solid var(--frame-grey);
  }
  .contact {
    position: absolute;
    right: 22px; top: 162px;
    color: var(--paper);
    text-align: right;
  }
  .contact .name {
    font-weight: 700;
    font-size: 18px;
    margin-bottom: 10px;
  }
  .contact .role {
    font-size: 15px;
    margin-bottom: 4px;
  }
  .contact .line {
    display: flex;
    justify-content: flex-end;
    align-items: center;
    gap: 8px;
    font-size: 14px;
    line-height: 22px;
  }
  .contact .icon { width: 13px; height: 13px; flex: none; }
</style>
</head>
<body>

  <section class="card card--back" aria-label="Card back">
    <div class="wordmark">BRAMLEIGH</div>
    <div class="baseline">real estate family office</div>
    <div class="web">www.bramleigh-estates.fr</div>
  </section>

  <section class="card card--front" aria-label="Card front">
    <div class="wordmark">BRAMLEIGH</div>
    <div class="baseline">real estate family office</div>
    <div class="contact-panel"></div>
    <div class="contact">
      <p class="name">Thibault Marchand</p>
      <p class="role">Real estate family office</p>
      <p class="line">+33(0)6.41.57.94.16
        <svg class="icon" viewBox="0 0 16 16" aria-hidden="true"><path fill="currentColor" d="M3 2l3 0 1 3-2 1.5c1 2 2.5 3.5 4.5 4.5L11 9l3 1v3c0 1-1 1.5-2 1.5C6 14 2 10 1.5 4 1.5 3 2 2 3 2z"/></svg>
      </p>
      <p class="line">tm@bramleigh-estates.fr
        <svg class="icon" viewBox="0 0 16 16" aria-hidden="true"><rect x="1" y="3" width="14" height="10" fill="currentColor"/><path d="M1.5 3.5L8 9l6.5-5.5" stroke="#0255a3" stroke-width="1.4" fill="none"/></svg>
      </p>
      <p class="line">www.bramleigh-estates.fr
        <svg class="icon" viewBox="0 0 16 16" aria-hidden="true"><circle cx="8" cy="8" r="7" fill="currentColor"/><path d="M1 8h14M8 1c-3 3-3 11 0 14M8 1c3 3 3 11 0 14" stroke="#0255a3" stroke-width="1.1" fill="none"/></svg>
      </p>
    </div>
  </section>

</body>
</html>
```